Real Estate "For Sale" Sign for construction company

We need a sign that we can use to hang on a post and place on the road when we sell a property. The sign will be simple and will need to mainly feature our logo (files attached), as well as the words "For Sale", and then our phone number "(555) 617 3489". The sign will hang on a post that'll look something like the attached picture.

Target Market(s)

Home buyers

Industry/Entity Type

Real Estate

Font styles to use
Serif
Sans Serif

Colors
0054AA
0677BA
7BADD7
CADEEF
E8F1F8
0094D4
00A9DD
6FCCEA
C7EBF8
E9F6FB

Requirements
Must have
• For Sale & our phone number

```html
<!DOCTYPE html>
<html lang="en">
<head>
<meta charset="utf-8">
<title>For Sale Sign – Highland Crest Properties</title>
<link href="https://fonts.googleapis.com/css2?family=Montserrat:wght@600;700;800&family=Open+Sans:wght@700&display=swap" rel="stylesheet">
<style>
  :root {
    --page-bg: #eef2f6;
    --sky-top: #8cc8ee;
    --sky-mid: #4f86c6;
    --ridge-blue: #2f5fa6;
    --navy: #17275c;
    --navy-deep: #142253;
    --accent: #00a9dd;
    --brand-blue: #0677ba;
    --white: #ffffff;
  }
  * { margin: 0; padding: 0; box-sizing: border-box; }
  html, body {
    width: 1200px; height: 1008px; overflow: hidden;
    background: var(--page-bg);
  }
  .sign {
    position: absolute;
    left: 300px; top: 52px;
    width: 600px; height: 904px;
    background: var(--white);
    box-shadow: 0 10px 30px rgba(20, 34, 83, 0.18);
    overflow: hidden;
  }
  .sign__hero {
    position: absolute; inset: 0 0 auto 0;
    height: 634px;
    background: linear-gradient(180deg,
      var(--sky-top) 0%,
      #6aa6dc 14%,
      var(--sky-mid) 30%,
      var(--ridge-blue) 46%,
      #223e83 58%,
      var(--navy) 68%,
      var(--navy-deep) 100%);
  }
  .sign__headline {
    position: absolute; left: 34px; top: 78px;
    font-family: "Montserrat", sans-serif;
    font-weight: 800;
    font-size: 172px;
    line-height: 0.98;
    letter-spacing: -2px;
    color: var(--white);
    text-shadow: 0 0 0 var(--navy), 3px 3px 0 var(--navy-deep);
  }
  .sign__cta {
    position: absolute; left: 36px; top: 476px;
    font-family: "Montserrat", sans-serif;
    font-weight: 700;
    font-size: 31px;
    color: var(--white);
    letter-spacing: 0.5px;
  }
  .sign__phone {
    position: absolute; left: 36px; top: 528px;
    display: flex; align-items: center; gap: 16px;
    font-family: "Open Sans", sans-serif;
    font-weight: 700;
    font-size: 56px;
    color: var(--white);
    letter-spacing: 0.5px;
  }
  .sign__phone-icon { width: 62px; height: 62px; flex: none; }
  .sign__divider {
    position: absolute; left: 0; right: 0; top: 634px;
    height: 5px; background: var(--brand-blue);
  }
  .sign__brand {
    position: absolute; left: 0; right: 0; top: 639px; bottom: 30px;
    display: flex; align-items: center; justify-content: center;
  }
  .brand-name {
    font-family: "Montserrat", sans-serif;
    font-weight: 600;
    font-size: 40px;
    color: var(--brand-blue);
    text-align: center;
    line-height: 1.2;
  }
  .sign__footer {
    position: absolute; left: 0; right: 0; bottom: 0;
    height: 30px;
    background: linear-gradient(180deg, var(--brand-blue) 0 5px, var(--navy) 5px);
  }
</style>
</head>
<body>
  <main class="sign">
    <div class="sign__hero" role="img" aria-label="Layered blue mountain ridges fading from light sky to deep navy"></div>

    <h1 class="sign__headline">FOR<br>SALE</h1>

    <p class="sign__cta">CALL US TODAY!</p>
    <p class="sign__phone">
      <svg class="sign__phone-icon" viewBox="0 0 62 62" aria-hidden="true">
        <circle cx="31" cy="31" r="31" fill="var(--accent)"/>
        <path d="M22 16c1.5-1 3.2-.6 4 .9l3 5.4c.7 1.3.4 2.9-.7 3.8l-2.2 1.7c1.6 3.6 4.4 6.5 8 8.2l1.7-2.2c.9-1.1 2.5-1.5 3.8-.8l5.4 2.9c1.5.8 2 2.6 1 4l-2 2.9c-1.1 1.6-3.1 2.4-5 1.9C29.6 42.3 19.8 32.5 17.4 23.1c-.5-1.9.3-3.9 1.9-5z" fill="var(--navy)"/>
      </svg>
      <span class="phone-number">(555) 617 3489</span>
    </p>

    <div class="sign__divider"></div>

    <div class="sign__brand">
      <p class="brand-name">Highland Crest Properties</p>
    </div>

    <div class="sign__footer"></div>
  </main>
</body>
</html>
```